Residential Construction Design

I'd like a business card that really explains what we do in residential construction. A big name and number, while the other information can be smaller. Since the logo is made up of grays and a teal color, the background may have to stay white? Maybe a subtle gray.(sending 2 different color schemes of the logo for different background color options) I would like a card that just appears "tough" when you look at it.

Industry/Entity Type

Residential

Contact Information for Business Card

Name and logo which will be provided.(Rex Pimbly Construction, LLC) Rex Pimbly -Licensed Contractor, Certified Home Inspector. (555) 310-7246 Email: Rpimbly_Construction@quorvane.com -Remodeling -Roofs - Siding -Drywall -Decks -Pole Barns -New Construction "Serving Southwest Michigan"

```html
<!DOCTYPE html>
<html lang="en">
<head>
<meta charset="utf-8">
<title>Rex Pimbly Construction, LLC — Business Card</title>
<link href="https://fonts.googleapis.com/css2?family=Open+Sans:wght@400;600;700&display=swap" rel="stylesheet">
<style>
  :root {
    --backdrop: #a3a3a3;
    --backdrop-dark: #8a8a8a;
    --card: #ffffff;
    --teal: #22c3b0;
    --teal-deep: #16978a;
    --ink: #3a3a3a;
    --ink-soft: #5a5a5a;
    --white: #ffffff;
  }
  * { box-sizing: border-box; margin: 0; padding: 0; }
  html, body { width: 1200px; height: 894px; overflow: hidden; }
  body {
    background: radial-gradient(circle at 50% 40%, var(--backdrop) 0%, var(--backdrop-dark) 100%);
    font-family: "Open Sans", Arial, sans-serif;
    position: relative;
  }
  .card {
    position: absolute;
    top: 298px;
    width: 520px;
    height: 297px;
    background: var(--card);
    box-shadow: 0 6px 18px rgba(0,0,0,0.25);
    overflow: hidden;
  }
  .card--front { left: 60px; }
  .card--back { left: 620px; }

  .brand {
    position: absolute;
    display: flex;
    align-items: center;
    gap: 16px;
  }
  .brand__mark {
    width: 64px;
    height: 64px;
    background: var(--teal);
    flex: none;
  }
  .brand__name {
    color: var(--ink);
    font-weight: 600;
    font-size: 22px;
    line-height: 1.15;
  }
  .card--front .brand { left: 44px; top: 30px; }
  .card--back .brand { right: 40px; top: 112px; flex-direction: column; gap: 12px; }
  .card--back .brand__mark { width: 96px; height: 96px; }
  .card--back .brand__name { font-size: 16px; text-align: center; }

  .person {
    position: absolute;
    left: 30px;
    top: 124px;
    color: var(--teal);
    display: flex;
    align-items: baseline;
    gap: 8px;
    white-space: nowrap;
  }
  .person__name { font-size: 22px; font-weight: 600; }
  .person__divider { font-size: 22px; font-weight: 600; }
  .person__title { font-size: 13px; font-weight: 400; }

  .services {
    position: absolute;
    left: 30px;
    top: 168px;
    font-size: 10.5px;
    font-weight: 700;
    color: var(--ink-soft);
    white-space: nowrap;
  }

  .band {
    position: absolute;
    left: 0;
    background: var(--teal);
    border-radius: 0 19px 19px 0;
    display: flex;
    align-items: center;
    white-space: nowrap;
  }
  .band--contact {
    top: 204px;
    width: 486px;
    height: 36px;
    padding-left: 14px;
    gap: 22px;
    font-size: 13px;
    font-weight: 600;
    color: var(--white);
  }
  .contact-item { display: flex; align-items: center; gap: 6px; }
  .contact-item--phone { font-size: 15px; font-weight: 700; }
  .contact-item svg { width: 16px; height: 16px; flex: none; }

  .band--area {
    top: 36px;
    width: 236px;
    height: 30px;
    padding-left: 22px;
    font-size: 13px;
    font-weight: 600;
    color: var(--ink);
  }
</style>
</head>
<body>

  <section class="card card--front" aria-label="Business card front">
    <div class="brand">
      <div class="brand__mark"></div>
      <div class="brand__name">Rex Pimbly<br>Construction, LLC</div>
    </div>

    <div class="person">
      <span class="person__name">Rex Pimbly</span>
      <span class="person__divider">|</span>
      <span class="person__title">Licensed Contractor · Certified Home Inspector</span>
    </div>

    <p class="services">Remodeling · Roofs · Siding · Drywall · Decks · Pole Barns · New Construction</p>

    <div class="band band--contact">
      <span class="contact-item contact-item--phone">
        <svg viewBox="0 0 16 16" aria-hidden="true"><circle cx="8" cy="8" r="8" fill="#16978a"/><path d="M5.2 4.2l1.4-.2.8 1.9-.9.7c.4.9 1.1 1.7 2 2.1l.7-.9 1.9.8-.2 1.4c-3.2.3-5.9-2.4-5.7-5.8z" fill="#fff"/></svg>
        (555) 310-7246
      </span>
      <span class="contact-item">
        <svg viewBox="0 0 16 16" aria-hidden="true"><circle cx="8" cy="8" r="8" fill="#16978a"/><rect x="4" y="5.2" width="8" height="5.6" rx="0.6" fill="#fff"/><path d="M4.3 5.6L8 8.4l3.7-2.8" stroke="#16978a" stroke-width="0.9" fill="none"/></svg>
        Rpimbly_Construction@quorvane.com
      </span>
    </div>
  </section>

  <section class="card card--back" aria-label="Business card back">
    <div class="band band--area">Serving Southwest Michigan</div>
    <div class="brand">
      <div class="brand__mark"></div>
      <div class="brand__name">Rex Pimbly<br>Construction, LLC</div>
    </div>
  </section>

</body>
</html>
```